RW dental business card. A family dental practice.

Logo plus the following details.

RW Dental
Dr. Marcus Ellory D.D.S
Family. Implant.Cosmetic

48 Fernbrook Lane, Unit 12-13
Lakeview, QX K2P7R4

Tel: 555-318-2670
Fx:555-318-9025
rwdental-sample.ca

On the double side:

Next app: ______________________

Please notify us at least 48hours in advance to avoid cancellation fees.

Target Market(s)

Family Dental Services

Industry/Entity Type

Dental

Contact Information for Business Card

Put logo prominently and all the info along with it.

Font styles to use
Other font styles liked:
• See Logo Font

Colors
0255a3
3277b5
85acd3
00a990
33b8a4

Requirements
Must have
• Logo and the info stated above.
• See the logo color scheme.
• Or a grayscale (Black, white gray) combination
Nice to have
• A modern unique layout
Should not have
• too simple a design

```html
<!DOCTYPE html>
<html lang="en">
<head>
<meta charset="utf-8">
<title>RW Dental – Business Card</title>
<link href="https://fonts.googleapis.com/css2?family=Roboto:wght@300;400;500;700&display=swap" rel="stylesheet">
<style>
  :root {
    --navy: #0255a3;
    --blue: #1257a6;
    --teal: #19ae96;
    --ink: #3a3d42;
    --tag: #555a60;
    --grey-line: #8a8d92;
    --rule: #2a2c30;
    --paper: #ffffff;
    --backdrop: #e8eaed;
  }
  * { box-sizing: border-box; margin: 0; padding: 0; }
  html, body { width: 1200px; height: 1000px; overflow: hidden; }
  body {
    background: var(--backdrop);
    font-family: "Roboto", Arial, sans-serif;
    position: relative;
  }
  .card {
    position: absolute;
    left: 250px;
    width: 700px;
    height: 400px;
    background: var(--paper);
    box-shadow: 0 6px 18px rgba(0,0,0,.14);
    overflow: hidden;
  }
  .card--front { top: 70px; }
  .card--back { top: 530px; }

  .card__bands { position: absolute; left: 0; bottom: 0; width: 700px; height: 80px; }

  /* front */
  .brand {
    position: absolute; left: 40px; top: 130px; width: 270px;
    display: flex; flex-direction: column; align-items: center;
  }
  .brand__mark {
    width: 64px; height: 64px; border-radius: 50%;
    background: var(--teal); margin-bottom: 14px;
  }
  .brand__name {
    font-size: 40px; font-weight: 500; color: var(--navy);
    letter-spacing: .5px; line-height: 1;
  }
  .brand__tagline {
    margin-top: 10px; font-size: 14px; font-weight: 500; color: var(--tag);
    letter-spacing: .3px; word-spacing: 3px;
  }
  .divider {
    position: absolute; left: 340px; top: 48px; width: 1px; height: 200px;
    background: var(--grey-line);
  }
  .person { position: absolute; left: 375px; top: 62px; }
  .person__name { font-size: 31px; font-weight: 700; color: var(--teal); line-height: 1.1; }
  .person__title { font-size: 21px; font-weight: 300; color: var(--teal); margin-top: 2px; }
  .contact { position: absolute; left: 378px; top: 150px; list-style: none; }
  .contact__item {
    display: flex; align-items: flex-start; gap: 10px;
    font-size: 17px; font-weight: 400; color: var(--ink); line-height: 1.2;
    margin-bottom: 6px;
  }
  .contact__icon {
    flex: none; width: 20px; height: 20px; border-radius: 50%;
    background: var(--teal); display: flex; align-items: center; justify-content: center;
  }
  .contact__icon svg { width: 12px; height: 12px; }

  /* back */
  .appointment__heading {
    position: absolute; left: 0; top: 28px; width: 312px; height: 76px;
    background: var(--blue); color: #fff;
    font-size: 25px; font-weight: 500;
    display: flex; align-items: center; padding-left: 38px;
  }
  .appointment__line {
    position: absolute; left: 38px; width: 274px; height: 1px; background: var(--rule);
  }
  .appointment__line--1 { top: 136px; }
  .appointment__line--2 { top: 170px; }
  .appointment__line--3 { top: 204px; }
</style>
</head>
<body>

<section class="card card--front" aria-label="Business card front">
  <div class="brand">
    <div class="brand__mark"></div>
    <div class="brand__name">RW Dental</div>
    <div class="brand__tagline">Family | Implant | Cosmetic</div>
  </div>

  <div class="divider"></div>

  <div class="person">
    <div class="person__name">Dr. Marcus Ellory</div>
    <div class="person__title">D.D.S</div>
  </div>

  <ul class="contact">
    <li class="contact__item">
      <span class="contact__icon"><svg viewBox="0 0 12 12"><path d="M1 4c0-2 2-2.5 5-2.5S11 2 11 4l-2.5.6L8 3.5H4l-.5 1.1L1 4zM3 6h6l1 4H2z" fill="#fff"/></svg></span>
      555-318-2670
    </li>
    <li class="contact__item">
      <span class="contact__icon"><svg viewBox="0 0 12 12"><rect x="3" y="1" width="6" height="3" fill="#fff"/><rect x="1" y="4.5" width="10" height="4.5" rx="1" fill="#fff"/><rect x="3" y="8" width="6" height="3" fill="#fff" stroke="#19ae96" stroke-width=".8"/></svg></span>
      555-318-9025
    </li>
    <li class="contact__item">
      <span class="contact__icon"><svg viewBox="0 0 12 12" fill="none" stroke="#fff" stroke-width="1"><circle cx="6" cy="6" r="4.8"/><ellipse cx="6" cy="6" rx="2" ry="4.8"/><path d="M1.2 6h9.6M2 3.6h8M2 8.4h8"/></svg></span>
      www.rwdental-sample.ca
    </li>
    <li class="contact__item">
      <span class="contact__icon"><svg viewBox="0 0 12 12"><path d="M6 11S2 6.8 2 4.5a4 4 0 0 1 8 0C10 6.8 6 11 6 11z" fill="#fff"/><circle cx="6" cy="4.5" r="1.5" fill="#19ae96"/></svg></span>
      <span>48 Fernbrook Lane, Unit 12-13<br>Lakeview, QX K2P7R4</span>
    </li>
  </ul>

  <svg class="card__bands" viewBox="0 0 700 80" aria-hidden="true">
    <rect x="0" y="46" width="420" height="34" fill="var(--teal)"/>
    <path d="M318 80 V28 Q318 0 350 0 H700 V80 Z" fill="var(--blue)"/>
  </svg>
</section>

<section class="card card--back" aria-label="Business card back">
  <div class="appointment__heading">Next Appointment</div>
  <div class="appointment__line appointment__line--1"></div>
  <div class="appointment__line appointment__line--2"></div>
  <div class="appointment__line appointment__line--3"></div>

  <svg class="card__bands" viewBox="0 0 700 80" aria-hidden="true">
    <rect x="0" y="54" width="340" height="26" fill="var(--teal)"/>
    <path d="M310 80 L318 46 Q324 32 344 32 H700 V80 Z" fill="var(--blue)"/>
  </svg>
</section>

</body>
</html>
```